Loomvista: fashion design product software needs your help

Fashion design product software company requests your assistance in designing a complete stationary package around our new logo design. Our software assists fashion designers and apparel houses with efficient communication and streamlined production between each other and manufacturers throughout the entire project design life cycle.

The look should reflect clean, simple and modern design. Not too "techie." Must use the provided logo and colors (or variations on the chosen colors, i.e. percentages as needed).

Reference website: www.loomvista-example.com

Buzzwords: manufacturing, production, apparel design/ers, streamlined process, effective communication, business, production software.

Please try to tone down or make the colors more subtle with more simple design style, layout. No sewing  theme. Thank you.

Target Market(s)

fashion designers and apparel houses that use software to manage and track production process life cycle.

Industry/Entity Type

Communication

Requirements
Must have
• Use of the logo and colors-or variations of colors (attached)
Nice to have
• Playfulness but corporate: with a sense of practicality, economical, streamlined production. Embossing considered.
Should not have
• Please keep in mind economics both financially and economically. Save trees and money! We believe in tactile paper but not "fashion-y" or sparkly, over-the-top colors, effects or production.

```html
<!DOCTYPE html>
<html lang="en">
<head>
<meta charset="utf-8">
<title>Loomvista Stationery</title>
<link href="https://fonts.googleapis.com/css2?family=Arimo:wght@400;700&display=swap" rel="stylesheet">
<style>
  :root {
    --backdrop: #80d3f1;
    --paper: #ffffff;
    --brown: #6b2e1f;
    --blue: #3db5e6;
    --shadow: rgba(60, 60, 60, 0.55);
    --rule: 2px;
  }
  * { margin: 0; padding: 0; box-sizing: border-box; }
  html, body {
    width: 1200px; height: 900px; overflow: hidden;
    background: var(--backdrop);
    font-family: "Arimo", Arial, sans-serif;
  }
  .canvas { position: relative; width: 1200px; height: 900px; }

  .sheet {
    position: absolute; background: var(--paper);
    border: 1px solid #222;
    box-shadow: -8px 8px 3px var(--shadow);
    overflow: hidden;
  }
  .letterhead { left: 141px; top: 9px; width: 647px; height: 876px; }
  .envelope  { left: 246px; top: 197px; width: 753px; height: 347px; }
  .card      { left: 499px; top: 364px; width: 666px; height: 431px; }

  .wordmark {
    position: absolute; font-weight: 700; color: var(--brown);
    letter-spacing: -0.01em; line-height: 1;
  }
  .dash { position: absolute; border-top: var(--rule) dashed; height: 0; }
  .dash.blue { border-color: var(--blue); }
  .dash.brown { border-color: var(--brown); }
  .ring {
    position: absolute; border-radius: 50%; background: var(--paper);
    border: var(--rule) solid;
  }
  .ring.blue { border-color: var(--blue); }
  .ring.brown { border-color: var(--brown); }

  /* Letterhead */
  .letterhead .wordmark { left: 42px; top: 26px; font-size: 28px; }
  .letterhead .footer-line {
    position: absolute; left: 218px; right: 8px; top: 854px;
    font-size: 6.6px; font-weight: 700; color: var(--blue);
    white-space: nowrap; line-height: 1;
  }
  .footer-line .sep { margin: 0 3px; }

  /* Envelope */
  .return-address {
    position: absolute; left: 26px; top: 17px;
    color: var(--blue); font-size: 8px; font-weight: 700; line-height: 12px;
  }
  .return-address .company { font-size: 9px; margin-bottom: 6px; }
  .envelope .wordmark { left: 88px; top: 295px; font-size: 17px; }

  /* Business card */
  .bar { position: absolute; right: 0; left: 332px; background: var(--brown); }
  .bar.top { top: 0; height: 11px; }
  .bar.bottom { bottom: 0; height: 13px; }
  .card .wordmark { left: 63px; top: 104px; font-size: 41px; }
  .holder {
    position: absolute; right: 370px; top: 268px; text-align: right; color: var(--brown);
  }
  .holder .name { font-size: 17px; font-weight: 700; letter-spacing: 0.12em; }
  .holder .role { font-size: 11px; font-weight: 700; margin-top: 6px; }
  .contact {
    position: absolute; left: 375px; top: 322px;
    color: var(--blue); font-size: 11px; font-weight: 700; line-height: 19px;
  }
  .contact .street { margin-bottom: 6px; }
</style>
</head>
<body>
<main class="canvas">

  <section class="sheet letterhead" aria-label="Letterhead">
    <div class="wordmark">Loomvista</div>
    <div class="dash brown" style="left:318px; top:24px; right:0;"></div>
    <div class="ring brown" style="left:300px; top:16px; width:18px; height:18px;"></div>
    <div class="dash blue" style="left:224px; top:38px; right:0;"></div>
    <div class="ring blue" style="left:206px; top:30px; width:18px; height:18px;"></div>

    <div class="dash blue" style="left:0; top:860px; width:184px;"></div>
    <div class="ring blue" style="left:184px; top:852px; width:17px; height:17px;"></div>
    <p class="footer-line">Loomvista Technologies Corp.<span class="sep">|</span>220 Harbor Street Portland, OR 97204<span class="sep">|</span>T: 555.014.2290<span class="sep">|</span>www.loomvista-example.com</p>
  </section>

  <section class="sheet envelope" aria-label="Envelope">
    <div class="return-address">
      <p class="company">Loomvista Technologies Corp.</p>
      <p>220 Harbor Street</p>
      <p>Portland, OR 97204</p>
      <p>T: 555.014.2290</p>
      <p>E: contact@loomvista-example.com</p>
      <p>www.loomvista-example.com</p>
    </div>
    <div class="dash blue" style="left:199px; top:25px; right:0;"></div>
    <div class="ring blue" style="left:180px; top:16px; width:19px; height:19px;"></div>

    <div class="dash brown" style="left:0; top:304px; width:52px;"></div>
    <div class="ring brown" style="left:52px; top:295px; width:20px; height:20px;"></div>
    <div class="wordmark">Loomvista</div>
  </section>

  <section class="sheet card" aria-label="Business card">
    <div class="bar top"></div>
    <div class="wordmark">Loomvista</div>
    <div class="holder">
      <p class="name">DANIEL R. OKAFOR</p>
      <p class="role">President</p>
    </div>
    <div class="ring brown" style="left:321px; top:279px; width:22px; height:22px;"></div>
    <div class="dash brown" style="left:343px; top:289px; right:0;"></div>

    <div class="dash blue" style="left:0; top:355px; width:321px;"></div>
    <div class="ring blue" style="left:321px; top:345px; width:22px; height:22px;"></div>

    <div class="contact">
      <p class="street">220 Harbor Street, Portland, OR 97204</p>
      <p>E: contact@loomvista-example.com</p>
      <p>T: 555.014.2290</p>
      <p>www.loomvista-example.com</p>
    </div>
    <div class="bar bottom"></div>
  </section>

</main>
</body>
</html>
```